Brunelle médico-conseils - word template

We are dooing lot of médical report from word document. We dont print the text on a stationnary. We are producting the report and save it in pdf. So I need à word template. I want something more than just hard the logo. I would like the look of a stationnary in the word template.

I put an exemple of report. But the final don't have to look that way. Propose something more acurate.
After that I will need a business card.

Industry/Entity Type

Medical

Requirements
Must have
• We have to do a design that integrate are logo and color. You have the file in the project.
• The wrihting beteen the title must be in times new roman.
Nice to have
• We have 2 offices:
• Québec (Building Mont-Soleil) 612, ave de Champlain, local 230, G2K 4P7 T.418 527-9143 T.418 527-9186
• St-Romuald (Building Carrefour Beaumont-Les rives) 2450, boul. du Versant-Est, local 310, G7A 3K2. T.418 726-5584 F.418 726-9017
• Mail: info@BrunelleMC.com and expertise@BrunelleMC.com
• Web: www.BrunelleMC.com
• For now you can type www.RDOT.ca to acces the web site.
Should not have
• The same look that the exemple. Because I want to upgrade the look of the company.

```html
<!DOCTYPE html>
<html lang="fr">
<head>
<meta charset="utf-8">
<title>Brunelle médico-conseils – papier à lettres</title>
<link rel="stylesheet" href="https://fonts.googleapis.com/css2?family=Arimo:wght@400;700&display=swap">
<style>
  :root {
    --brand-blue: #2b6fa8;
    --brand-orange: #f5a320;
    --grid-blue: #dbe6f1;
    --grid-warm: #fbe9c8;
    --page: #ffffff;
    --watermark: #eef2f7;
  }
  html, body { margin: 0; padding: 0; overflow: hidden; }
  body { width: 927px; height: 1200px; background: var(--page); font-family: "Arimo", Arial, sans-serif; }
  .letterhead { position: relative; width: 927px; height: 1200px; overflow: hidden; background: var(--page); }

  .texture-top, .texture-bottom { position: absolute; left: 0; width: 927px; }
  .texture-top {
    top: 0; height: 197px;
    background:
      linear-gradient(180deg, rgba(255,255,255,0) 0%, #fff 100%),
      linear-gradient(90deg, var(--grid-blue) 0%, var(--grid-warm) 45%, var(--grid-blue) 75%, var(--grid-blue) 100%);
  }
  .texture-bottom {
    top: 968px; height: 123px;
    background:
      linear-gradient(0deg, rgba(255,255,255,0) 0%, #fff 100%),
      linear-gradient(90deg, var(--grid-blue) 0%, var(--grid-warm) 45%, var(--grid-blue) 75%, var(--grid-blue) 100%);
  }

  .brand { position: absolute; left: 30px; top: 28px; height: 70px; padding-right: 14px; display: flex; align-items: center; gap: 14px; background: var(--page); }
  .brand-square { width: 50px; height: 50px; background: var(--brand-orange); }
  .brand-name { font-size: 38px; font-weight: 700; color: var(--brand-blue); letter-spacing: -0.5px; }

  .watermark-block { position: absolute; left: 315px; top: 450px; width: 298px; height: 298px; background: var(--watermark); }

  .footer { position: absolute; left: 0; top: 1091px; width: 927px; height: 109px; background: var(--brand-blue); border-top: 4px solid var(--brand-orange); box-sizing: border-box; color: #fff; font-size: 13px; font-weight: 700; line-height: 17.5px; }
  .footer-strip { position: absolute; left: 0; bottom: 0; width: 100%; height: 9px; background: var(--brand-orange); }
  .office { position: absolute; top: 21px; }
  .office-quebec { left: 23px; }
  .office-rive { right: 23px; text-align: right; }
  .office-city { color: var(--brand-orange); }
  .phones { display: flex; justify-content: space-between; gap: 40px; }
  .label { color: var(--brand-orange); }
  .contact { position: absolute; top: 32px; left: 0; width: 927px; text-align: center; color: var(--brand-orange); line-height: 16.5px; }
</style>
</head>
<body>
<div class="letterhead">
  <div class="texture-top" role="img" aria-label="Motif de grille fine bleu et orangé en haut de page"></div>
  <div class="texture-bottom" role="img" aria-label="Motif de grille fine bleu et orangé en bas de page"></div>

  <header class="brand">
    <span class="brand-square"></span>
    <span class="brand-name">Brunelle médico-conseils</span>
  </header>

  <div class="watermark-block" aria-hidden="true"></div>

  <footer class="footer">
    <div class="office office-quebec">
      <div class="office-city">Québec</div>
      <div>(Building Mont-Soleil)</div>
      <div>612, ave de Champlain, local 230, G2K 4P7</div>
      <div class="phones"><span><span class="label">[T]</span> 418 527-9143</span><span><span class="label">[F]</span> 418 527-9186</span></div>
    </div>
    <div class="contact">
      <div>info@BrunelleMC.com</div>
      <div>expertise@BrunelleMC.com</div>
      <div>www.BrunelleMC.com</div>
    </div>
    <div class="office office-rive">
      <div class="office-city">St-Romuald</div>
      <div>(Building Carrefour Beaumont-Les rives)</div>
      <div>2450, boul. du Versant-Est, local 310, G7A 3K2</div>
      <div class="phones"><span><span class="label">[T]</span> 418 726-5584</span><span><span class="label">[F]</span> 418 726-9017</span></div>
    </div>
    <div class="footer-strip"></div>
  </footer>
</div>
</body>
</html>
```